I'm looking for a movie poster for my short film, "The Tin Lamp."

Requirements
Must have
• MARBLE OAK PRODUCTIONS presents a film written and directed by TESSA VARLOWE starring GORDON ALVERSTAD, PHILIP ORTEGRAY and MARIBETH KOLSTRAND "THE TIN LAMP" 1st assistant director NOELLE PRATTICK director of photography TAVION REESH edited by ELLIOT PRUE executive producers KAT & WALTER FENSHAW produced by OSCAR TAMBELLI and TESSA VARLOWE

```html
<!DOCTYPE html>
<html lang="en">
<head>
<meta charset="utf-8">
<title>The Tin Lamp — Poster</title>
<link rel="stylesheet" href="https://fonts.googleapis.com/css2?family=Antonio:wght@600&family=Encode+Sans+Condensed:wght@400&family=Fira+Sans+Condensed:wght@400&display=swap">
<style>
  :root {
    --ink: #ffffff;
    --night: #140d10;
    --ember: #d4391f;
    --amber: #f08a4a;
    --dusk: #2a3557;
    --steel: #4f6f93;
    --haze: #8a6c7a;
  }
  html, body {
    margin: 0;
    padding: 0;
    width: 849px;
    height: 1200px;
    overflow: hidden;
    background: var(--night);
  }
  .poster {
    position: relative;
    width: 849px;
    height: 1200px;
    overflow: hidden;
    color: var(--ink);
  }
  .poster-backdrop {
    position: absolute;
    inset: 0;
    background:
      radial-gradient(ellipse 260px 180px at 40px 230px, rgba(240,120,70,0.75), transparent 70%),
      radial-gradient(ellipse 420px 210px at 560px 560px, rgba(225,70,35,0.85), transparent 70%),
      radial-gradient(ellipse 160px 200px at 120px 780px, rgba(220,120,80,0.55), transparent 70%),
      radial-gradient(ellipse 300px 260px at 700px 960px, rgba(160,80,90,0.45), transparent 70%),
      radial-gradient(ellipse 500px 300px at 300px 900px, rgba(70,95,140,0.7), transparent 75%),
      linear-gradient(180deg, #1c1012 0%, #3a1412 18%, #8a2a1c 38%, #6b2c2a 52%, var(--dusk) 68%, var(--steel) 86%, #8aa0b8 100%);
  }
  .poster-title {
    position: absolute;
    left: 0;
    width: 849px;
    margin: 0;
    font-family: "Antonio", "Oswald", sans-serif;
    font-weight: 600;
    line-height: 1;
    text-align: center;
    white-space: nowrap;
    color: var(--ink);
  }
  .poster-title span { position: absolute; left: 0; width: 100%; }
  .title-first { top: 128px; font-size: 228px; }
  .title-second { top: 350px; font-size: 228px; letter-spacing: 4px; }
  .tagline {
    position: absolute;
    right: 97px;
    top: 616px;
    margin: 0;
    font-family: "Encode Sans Condensed", "Fira Sans Condensed", sans-serif;
    font-size: 37px;
    line-height: 45px;
    text-align: right;
    color: var(--ink);
  }
  .tagline span { display: block; }
  .credits {
    position: absolute;
    left: 78px;
    width: 693px;
    top: 1030px;
    margin: 0;
    font-family: "Fira Sans Condensed", "Arial Narrow", sans-serif;
    font-size: 14.6px;
    line-height: 21px;
    text-align: center;
    text-transform: uppercase;
    color: var(--ink);
  }
</style>
</head>
<body>
  <main class="poster">
    <div class="poster-backdrop" role="img" aria-label="Blurred photograph of a dimly lit bar with silhouetted patrons, warm red neon light and cool blue shadows"></div>

    <h1 class="poster-title">
      <span class="title-first">THE</span>
      <span class="title-second">TIN LAMP</span>
    </h1>

    <p class="tagline">
      <span>Friends don’t let</span>
      <span>friends fly solo.</span>
    </p>

    <p class="credits">MARBLE OAK PRODUCTIONS presents a film written and directed by TESSA VARLOWE starring GORDON ALVERSTAD, PHILIP ORTEGRAY and MARIBETH KOLSTRAND "THE TIN LAMP" 1st assistant director NOELLE PRATTICK director of photography TAVION REESH edited by ELLIOT PRUE executive producers KAT &amp; WALTER FENSHAW produced by OSCAR TAMBELLI and TESSA VARLOWE</p>
  </main>
</body>
</html>
```